Flyer für Immobilienmakler
Top Arbeit vom Designer. Er hat alle Idee schnell und professionell umgesetzt und das Ergebnis kann sich sehen lassen. Herzlichen Dank für die großartige Arbeit. Immer wieder gerne.
Zielgruppe
Immobilienmakler, Zielgruppe sind Menschen die uns weiterempfehlen um ihre Immobilie zu verkaufen
Aufgabenstellung
Ein Flyer DIN lang quer, Vorder und Rückseite, Es geht um eine Tippgeberprovision welche Menschen bekommen die uns einen Verkaufskunden bringen, diese erhalten 10 %- genaue Texte und Hinweise werde ich einbringen, Unser Slogan: 'Unsere Erfahrung für Ihren Vorteil'
Nachtrag. Bei dem Flyer 'Vom Berg Immobilien' finde ich die blauen Banner/ Streifen gut- ist aber kein Muss. Update: Es war als Inspiration von meiner Seite gedacht. Auf keinen Fall darf es genauso aussehen!!
Meine jetzige Webseite ist auch gut um die Farben zu erkennen, jedoch nicht unbedingt das Design, da ich gerade eine neue Webseite erstellen lasse

```html
<!DOCTYPE html>
<html lang="de">
<head>
<meta charset="utf-8">
<title>Aurel Immobilien – Flyer DIN lang, Vorder- und Rückseite</title>
<link rel="stylesheet" href="https://fonts.googleapis.com/css2?family=Poppins:wght@400;500;600;700&display=swap">
<style>
  :root {
    --navy: #25264f;
    --navy-deep: #222347;
    --taupe: #b9a89b;
    --taupe-light: #cfc1b6;
    --taupe-dark: #a8968a;
    --steel: #7f97a8;
    --white: #ffffff;
    --backdrop: #8e8e8e;
  }
  * { box-sizing: border-box; margin: 0; padding: 0; }
  html, body { width: 1200px; height: 1117px; overflow: hidden; }
  body {
    background: var(--backdrop);
    font-family: "Poppins", sans-serif;
    position: relative;
  }
  .flyer {
    position: absolute;
    left: 156px;
    width: 888px;
    height: 444px;
    background: var(--white);
    overflow: hidden;
  }
  .flyer--front { top: 77px; }
  .flyer--back { top: 568px; }
  .flyer__shapes { position: absolute; inset: 0; width: 888px; height: 444px; }

  .brand {
    position: absolute;
    color: var(--navy);
    font-weight: 600;
    font-size: 26px;
    line-height: 1;
    letter-spacing: 0.2px;
    white-space: nowrap;
    display: flex;
    align-items: center;
    gap: 10px;
  }
  .brand__mark {
    width: 14px; height: 14px; border-radius: 50%;
    background: var(--taupe);
    flex: none;
  }
  .flyer--front .brand { left: 64px; top: 62px; }
  .flyer--back .brand { left: 579px; top: 320px; }

  .slogan {
    position: absolute;
    left: 60px; top: 149px;
    color: var(--white);
    font-weight: 700;
    font-size: 36px;
    line-height: 37px;
    text-transform: uppercase;
    letter-spacing: 0.2px;
  }
  .slogan__accent { color: var(--taupe); }

  .intro {
    position: absolute;
    left: 60px; top: 295px;
    color: var(--navy);
    font-size: 19px;
    line-height: 22px;
    font-weight: 400;
  }

  .offer {
    position: absolute;
    left: 520px; top: 22px;
    width: 340px;
    text-align: center;
    color: var(--white);
  }
  .offer__lead { font-weight: 600; font-size: 44px; line-height: 1; margin-top: 18px; }
  .offer__value {
    font-weight: 700;
    font-size: 132px;
    line-height: 1;
    letter-spacing: -4px;
    margin-top: -6px;
    margin-left: -20px;
    margin-right: -20px;
    background: linear-gradient(180deg, var(--taupe-light), var(--taupe-dark));
    -webkit-background-clip: text;
    background-clip: text;
    color: transparent;
  }
  .offer__note { font-size: 15px; line-height: 17px; margin-top: 0; }
  .offer__note strong { font-weight: 600; }

  .contact {
    position: absolute;
    left: 0; top: 381px;
    width: 888px; height: 63px;
    color: var(--white);
    font-weight: 700;
    font-size: 19.5px;
  }
  .contact__item {
    position: absolute;
    top: 0; height: 63px;
    display: flex; align-items: center; gap: 10px;
    white-space: nowrap;
  }
  .contact__item--phone { left: 60px; }
  .contact__item--mail { left: 374px; }
  .contact__item--web { left: 670px; }
  .contact__divider {
    position: absolute; left: 652px; top: 18px;
    width: 1.5px; height: 28px; background: var(--white);
  }
  .contact__icon { width: 20px; height: 20px; flex: none; }
</style>
</head>
<body>

<!-- Vorderseite -->
<section class="flyer flyer--front">
  <svg class="flyer__shapes" viewBox="0 0 888 444">
    <defs>
      <linearGradient id="houseTones" x1="0" y1="0" x2="0" y2="1">
        <stop offset="0" stop-color="#b7c9e3"/>
        <stop offset="0.55" stop-color="#e8dfd8"/>
        <stop offset="0.82" stop-color="#8f9c63"/>
        <stop offset="1" stop-color="#c9c3bc"/>
      </linearGradient>
    </defs>
    <polygon points="0,0 695,0 688,12 0,12" fill="var(--navy)"/>
    <polygon points="702,0 888,0 888,12 695,12" fill="var(--taupe)"/>
    <polygon role="img" aria-label="Foto: modernes weißes Einfamilienhaus mit Holzpergola und Gräsern vor blauem Himmel"
      points="354,22 888,22 888,380 439,380 476,283" fill="url(#houseTones)"/>
    <polygon points="340,24 347,24 398,128 391,128" fill="var(--navy)"/>
    <polygon points="0,139 396,139 460,283 0,283" fill="var(--navy)"/>
    <polygon points="451,297 458,297 422,380 415,380" fill="var(--navy)"/>
    <polygon points="0,381 345,381 318,444 0,444" fill="var(--taupe)"/>
    <polygon points="357,381 888,381 861,444 330,444" fill="var(--navy)"/>
    <polygon points="870,444 888,410 888,444" fill="var(--taupe)"/>
  </svg>

  <div class="brand"><span class="brand__mark"></span>Aurel Immobilien</div>

  <h1 class="slogan">Unsere<br>Erfahrung für<br><span class="slogan__accent">Ihren Vorteil</span></h1>

  <p class="intro">Wir unterstützen Sie im<br>gesamten Prozess mit unserem<br>einzigartigen Modulsystem.</p>

  <div class="contact">
    <div class="contact__item contact__item--phone">
      <svg class="contact__icon" viewBox="0 0 20 20"><circle cx="10" cy="10" r="10" fill="var(--white)"/><path d="M7 5.5l1.6 2.4-1 1.1c.6 1.3 1.6 2.3 2.9 2.9l1.1-1 2.4 1.6-.8 1.8c-3.8-.4-6.7-3.3-7.1-7.1z" fill="var(--taupe)"/></svg>
      +49 (0)6251 5550198
    </div>
    <div class="contact__item contact__item--mail">
      <svg class="contact__icon" viewBox="0 0 20 20"><circle cx="10" cy="10" r="10" fill="var(--taupe-light)"/><rect x="5" y="6.5" width="10" height="7" fill="none" stroke="var(--navy)" stroke-width="1.2"/><path d="M5 6.5l5 4 5-4" fill="none" stroke="var(--navy)" stroke-width="1.2"/></svg>
      kontakt@aurel.immo
    </div>
    <span class="contact__divider"></span>
    <div class="contact__item contact__item--web">
      <svg class="contact__icon" viewBox="0 0 20 20"><circle cx="10" cy="10" r="10" fill="var(--taupe-light)"/><g fill="none" stroke="var(--navy)" stroke-width="1.1"><circle cx="10" cy="10" r="5"/><ellipse cx="10" cy="10" rx="2.2" ry="5"/><path d="M5 10h10"/></g></svg>
      aurel.immo
    </div>
  </div>
</section>

<!-- Rückseite -->
<section class="flyer flyer--back">
  <svg class="flyer__shapes" viewBox="0 0 888 444">
    <defs>
      <linearGradient id="interiorTones" x1="0" y1="0" x2="1" y2="1">
        <stop offset="0" stop-color="#eceae7"/>
        <stop offset="0.5" stop-color="#b4b1ad"/>
        <stop offset="1" stop-color="#dcd8d2"/>
      </linearGradient>
    </defs>
    <polygon points="0,0 188,0 195,12 0,12" fill="var(--taupe)"/>
    <polygon points="196,0 888,0 888,12 203,12" fill="var(--navy)"/>
    <polygon role="img" aria-label="Foto: helles Wohnzimmer mit Marmorkamin, weißem Sofa und offener Küche"
      points="0,22 516,22 440,183 530,380 0,380" fill="url(#interiorTones)"/>
    <polygon points="532,22 888,22 888,284 502,284 455,183" fill="var(--navy)"/>
    <polygon points="526,22 532,22 466,160 460,160" fill="var(--steel)"/>
    <polygon points="507,298 514,298 554,380 547,380" fill="var(--navy)"/>
    <polygon points="0,381 345,381 318,444 0,444" fill="var(--taupe)"/>
    <polygon points="357,381 888,381 861,444 330,444" fill="var(--navy)"/>
    <polygon points="870,444 888,410 888,444" fill="var(--taupe)"/>
  </svg>

  <div class="offer">
    <p class="offer__lead">Erhalten</p>
    <p class="offer__value">10%-</p>
    <p class="offer__note">indem Sie es den Menschen empfehlen,<br>die Ihnen am nächsten stehen<br><strong>ihr Eigentum an uns zu verkaufen</strong></p>
  </div>

  <div class="brand"><span class="brand__mark"></span>Aurel Immobilien</div>

  <div class="contact">
    <div class="contact__item contact__item--phone">
      <svg class="contact__icon" viewBox="0 0 20 20"><circle cx="10" cy="10" r="10" fill="var(--white)"/><path d="M7 5.5l1.6 2.4-1 1.1c.6 1.3 1.6 2.3 2.9 2.9l1.1-1 2.4 1.6-.8 1.8c-3.8-.4-6.7-3.3-7.1-7.1z" fill="var(--taupe)"/></svg>
      +49 (0)6251 5550198
    </div>
    <div class="contact__item contact__item--mail">
      <svg class="contact__icon" viewBox="0 0 20 20"><circle cx="10" cy="10" r="10" fill="var(--taupe-light)"/><rect x="5" y="6.5" width="10" height="7" fill="none" stroke="var(--navy)" stroke-width="1.2"/><path d="M5 6.5l5 4 5-4" fill="none" stroke="var(--navy)" stroke-width="1.2"/></svg>
      kontakt@aurel.immo
    </div>
    <span class="contact__divider"></span>
    <div class="contact__item contact__item--web">
      <svg class="contact__icon" viewBox="0 0 20 20"><circle cx="10" cy="10" r="10" fill="var(--taupe-light)"/><g fill="none" stroke="var(--navy)" stroke-width="1.1"><circle cx="10" cy="10" r="5"/><ellipse cx="10" cy="10" rx="2.2" ry="5"/><path d="M5 10h10"/></g></svg>
      aurel.immo
    </div>
  </div>
</section>

</body>
</html>
```